TR Advisory Business Cards - High End AV / Low Voltage Company

We are low voltage AV company that specializes in high end clients on the residential side and larger businesses on the commercial side. We want something modern, tech looking but also something that is extremely professional looking. We have uploaded our logos and postcards we already have in the field. Along with a picture of one of our wrapped vans. Our website is at www.trvadvisory.example and our primary colors are the orange, green, grey and blue all military color finishes.

We are interesting in the slogans "Pairing You with the Right Technology" or "Leading the Lowcountry in Tech"

Target Market(s)

We focus on 70% Commercial and 30% Residential Customers

Industry/Entity Type

Low Voltage, AV Company

Contact Information for Business Card

Name - Dorian Fairweather, Title - Owner, Office Phone - 555-714-3096, Mobile Phone - 555-802-4173, E-Mail - d@trvadvisory.example, Website: www.trvadvisory.example

Font styles to use
Sans Serif

Requirements
Must have
• Must have Name, Title, Work Phone & Mobile, Website and Logo.
Nice to have
• We want something that will impress our higher end clients with a great logo
Should not have
• Too traditional or plain.

```html
<!DOCTYPE html>
<html lang="en">
<head>
<meta charset="utf-8">
<title>TR Advisory Business Cards</title>
<link rel="stylesheet" href="https://fonts.googleapis.com/css2?family=Montserrat:wght@400;500;700;800&family=Arimo:wght@400;700&display=swap">
<style>
  :root {
    --rust: #c4592e;
    --orange: #e8682c;
    --silver: #d9d9d9;
    --steel: #9a9a9a;
    --ink: #1c1c1c;
    --paper: #ffffff;
    --backdrop: #dde2e3;
  }
  * { margin: 0; padding: 0; box-sizing: border-box; }
  html, body { width: 1200px; height: 675px; overflow: hidden; }
  body {
    background: var(--backdrop);
    display: flex;
    align-items: center;
    justify-content: center;
    gap: 40px;
    font-family: "Arimo", Arial, sans-serif;
  }
  .card {
    width: 540px;
    height: 309px;
    position: relative;
    box-shadow: 0 8px 24px rgba(0,0,0,0.18);
  }

  /* Front */
  .card-front {
    background: var(--rust);
    display: flex;
    flex-direction: column;
    align-items: center;
    justify-content: center;
    color: var(--silver);
  }
  .brand-mark {
    display: flex;
    align-items: center;
    gap: 14px;
  }
  .brand-mark .ring {
    width: 58px; height: 58px;
    border-radius: 50%;
    border: 4px solid var(--silver);
  }
  .brand-mark .brand-name {
    font-family: "Montserrat", sans-serif;
    font-weight: 700;
    font-size: 34px;
    letter-spacing: 3px;
    text-transform: uppercase;
    color: var(--silver);
  }
  .tagline-row {
    display: flex;
    align-items: center;
    gap: 12px;
    margin-top: 22px;
    width: 100%;
    padding: 0 44px;
  }
  .tagline-row .rule { flex: 1; height: 2px; background: var(--steel); }
  .tagline {
    font-size: 17px;
    font-weight: 700;
    color: var(--silver);
    white-space: nowrap;
  }
  .services {
    margin-top: 12px;
    text-align: center;
    font-size: 12.5px;
    line-height: 1.5;
    color: #e8c9b8;
  }

  /* Back */
  .card-back {
    background: var(--paper);
    display: flex;
    align-items: center;
    padding: 0 40px;
  }
  .back-brand {
    width: 150px;
    display: flex;
    flex-direction: column;
    align-items: center;
    gap: 10px;
  }
  .back-brand .ring {
    width: 74px; height: 74px;
    border-radius: 50%;
    border: 5px solid var(--orange);
  }
  .back-brand .brand-name {
    font-family: "Montserrat", sans-serif;
    font-weight: 700;
    font-size: 20px;
    letter-spacing: 2px;
    text-transform: uppercase;
    color: var(--orange);
    text-align: center;
  }
  .divider {
    width: 2px;
    height: 140px;
    background: var(--orange);
    margin: 0 26px 0 22px;
  }
  .contact-block { display: flex; flex-direction: column; }
  .person-name {
    font-family: "Montserrat", sans-serif;
    font-weight: 400;
    font-size: 27px;
    letter-spacing: 2px;
    color: var(--orange);
    line-height: 1.1;
  }
  .person-title {
    font-family: "Montserrat", sans-serif;
    font-weight: 800;
    font-size: 21px;
    color: var(--orange);
    margin-bottom: 18px;
  }
  .contact-line {
    display: flex;
    align-items: center;
    gap: 8px;
    font-size: 14px;
    color: var(--ink);
    line-height: 1.6;
  }
  .contact-line svg { width: 14px; height: 14px; fill: var(--orange); flex: none; }
  .web-domain { color: var(--orange); }
</style>
</head>
<body>

<section class="card card-front">
  <div class="brand-mark">
    <span class="ring"></span>
    <span class="brand-name">TR Advisory</span>
  </div>
  <div class="tagline-row">
    <span class="rule"></span>
    <span class="tagline">Leading the Lowcountry in Tech</span>
    <span class="rule"></span>
  </div>
  <p class="services">
    Home Automation • Surveilliance Systems • Home<br>
    Networks • Sound Speacialists • Structured wiring
  </p>
</section>

<section class="card card-back">
  <div class="back-brand">
    <span class="ring"></span>
    <span class="brand-name">TR Advisory</span>
  </div>
  <span class="divider"></span>
  <div class="contact-block">
    <h1 class="person-name">Dorian Fairweather</h1>
    <h2 class="person-title">Owner</h2>
    <p class="contact-line">
      <svg viewBox="0 0 24 24" aria-hidden="true"><path d="M6.6 10.8a15.1 15.1 0 0 0 6.6 6.6l2.2-2.2a1 1 0 0 1 1-.25 11.4 11.4 0 0 0 3.6.57 1 1 0 0 1 1 1V20a1 1 0 0 1-1 1A17 17 0 0 1 3 4a1 1 0 0 1 1-1h3.5a1 1 0 0 1 1 1c0 1.25.2 2.45.57 3.6a1 1 0 0 1-.25 1z"/></svg>
      555-714-3096 ; 555-802-4173
    </p>
    <p class="contact-line">
      <svg viewBox="0 0 24 24" aria-hidden="true"><path d="M2 5h20v14H2z M2 5l10 8 10-8" /></svg>
      d@trvadvisory.example
    </p>
    <p class="contact-line">
      <svg viewBox="0 0 24 24" aria-hidden="true"><path d="M12 2a10 10 0 1 0 0 20 10 10 0 0 0 0-20zm6.9 6h-3a15.7 15.7 0 0 0-1.4-3.6A8 8 0 0 1 18.9 8zM12 4a14 14 0 0 1 1.9 4h-3.8A14 14 0 0 1 12 4zM4.3 14a8 8 0 0 1 0-4h3.4a16 16 0 0 0 0 4zm.8 2h3a15.7 15.7 0 0 0 1.4 3.6A8 8 0 0 1 5.1 16zm3-8h-3a8 8 0 0 1 4.4-3.6A15.7 15.7 0 0 0 8.1 8zM12 20a14 14 0 0 1-1.9-4h3.8A14 14 0 0 1 12 20zm2.3-6H9.7a14.6 14.6 0 0 1 0-4h4.6a14.6 14.6 0 0 1 0 4zm.2 5.6a15.7 15.7 0 0 0 1.4-3.6h3a8 8 0 0 1-4.4 3.6zm1.8-5.6a16 16 0 0 0 0-4h3.4a8 8 0 0 1 0 4z"/></svg>
      <span>www.<span class="web-domain">trvadvisory</span>.example</span>
    </p>
  </div>
</section>

</body>
</html>
```